Amber Burrows Business Card Design

Amber Burrows - Gathering Gentle Meadow Corners

Amber Burrows is a company that focuses on promoting the design, construction, consultation and support of natural, creative and organic play spaces for Early Childhood and learning environments.

We need a professional Business Card designed that is unique modern and creative. The Philosophy of the company is nostalgic so the business and will need to reflect this but also reflect that our ideas are modern and cutting edge.

The business card will need to be a talking point, by either having a unique size, quality and/or placement of logo or other quality.

I am more interested in using natural recycled paper, as this would reflect the philosophy of the company, but I open to seeing colour used creatively.
Updates

Hi Designers, Apologies, Could you please add www.amberburrows.com.au to the business card. Thanks very much.

Hi All, Thank you all for your submission thus far. Please note the fonts for used in the logo are: Ostrich Sans Black and Archer Semi Bold. If these could be considered for contact details, my name etc. Also please show the design on a recycled brown card if possible as this will be the type of card I will use when printing. Thanks so much.

Target Market(s)

Child Care Providers, Play Industry Professionals

Industry/Entity Type

Business

Contact Information for Business Card

Amber Burrows
Gathering Gentle Meadow Corners
Marguerite Holloway
0419 862 503
marguerite@amberburrows.com.au

Font styles to use
Sans Serif

Requirements
Must have
• The Logo and the Details plus the below phrase
• Amber Burrows - Gathering Gentle Meadow Corners
Nice to have
• A bit of colour, but not too much colour.
Should not have
• Not to have a white background, recycled brown card only

```html
<!DOCTYPE html>
<html lang="en">
<head>
<meta charset="utf-8">
<title>Amber Burrows Business Card Design</title>
<link rel="stylesheet" href="https://fonts.googleapis.com/css2?family=Oswald:wght@300;500;600&family=Zilla+Slab:wght@400;600&display=swap">
<style>
  :root {
    --backdrop: #ece6dd;
    --kraft: #c7b294;
    --kraft-edge: #b59f80;
    --leaf-green: #2f6b2b;
    --ink: #1b1a18;
    --graphite: #5c5750;
    --silhouette: #24201b;
  }
  * { box-sizing: border-box; margin: 0; padding: 0; }
  html, body {
    width: 1200px;
    height: 800px;
    overflow: hidden;
    background: var(--backdrop);
  }
  .canvas {
    width: 1200px;
    height: 800px;
    display: flex;
    flex-direction: column;
    align-items: center;
    justify-content: center;
    gap: 36px;
  }
  .card {
    position: relative;
    width: 590px;
    height: 360px;
    background: var(--kraft);
    border: 1px solid var(--kraft-edge);
    box-shadow: 0 2px 6px rgba(60, 45, 25, 0.18);
    overflow: hidden;
  }

  /* Front face */
  .card-front .tree-illustration {
    position: absolute;
    left: 0;
    top: 0;
    width: 280px;
    height: 210px;
    background: linear-gradient(135deg, var(--silhouette) 0%, #3a332b 100%);
    border-bottom-right-radius: 60px;
  }
  .card-front .brand-block {
    position: absolute;
    right: 40px;
    bottom: 48px;
    text-align: left;
  }
  .brand-name {
    font-family: "Oswald", sans-serif;
    font-weight: 600;
    color: var(--leaf-green);
    letter-spacing: 1px;
    text-transform: uppercase;
    line-height: 1;
    white-space: nowrap;
  }
  .card-front .brand-name { font-size: 40px; }
  .tagline {
    font-family: "Zilla Slab", serif;
    font-weight: 600;
    color: var(--leaf-green);
    text-transform: uppercase;
    line-height: 1.05;
  }
  .card-front .tagline {
    font-size: 12px;
    text-align: right;
    margin-top: 4px;
  }
  .card-front .web-address {
    font-family: "Oswald", sans-serif;
    font-weight: 300;
    font-size: 15px;
    letter-spacing: 3px;
    color: var(--graphite);
    text-transform: uppercase;
    margin-top: 10px;
  }

  /* Back face */
  .card-back .logo-block {
    position: absolute;
    left: 36px;
    top: 112px;
    width: 230px;
    display: flex;
    flex-direction: column;
    align-items: center;
  }
  .logo-dot {
    width: 34px;
    height: 34px;
    border-radius: 50%;
    background: var(--leaf-green);
    margin-bottom: 12px;
  }
  .card-back .brand-name { font-size: 30px; }
  .card-back .tagline {
    font-size: 10px;
    text-align: center;
    margin-top: 4px;
  }
  .contact-block {
    position: absolute;
    left: 300px;
    top: 124px;
  }
  .person-name {
    font-family: "Oswald", sans-serif;
    font-weight: 500;
    font-size: 23px;
    letter-spacing: 1px;
    color: var(--ink);
    text-transform: uppercase;
    margin-bottom: 16px;
    white-space: nowrap;
  }
  .contact-line {
    font-family: "Zilla Slab", serif;
    font-weight: 400;
    font-size: 15px;
    color: var(--graphite);
    line-height: 1.55;
    white-space: nowrap;
  }
</style>
</head>
<body>
<main class="canvas">
  <section class="card card-front" aria-label="Business card front">
    <div class="tree-illustration" role="img" aria-label="Dark silhouette illustration of a leafy tree with a child climbing it"></div>
    <div class="brand-block">
      <div class="brand-name">Amber Burrows</div>
      <div class="tagline">Gathering<br>Gentle Meadow Corners</div>
      <div class="web-address">www.amberburrows.com.au</div>
    </div>
  </section>

  <section class="card card-back" aria-label="Business card back">
    <div class="logo-block">
      <div class="logo-dot"></div>
      <div class="brand-name">Amber Burrows</div>
      <div class="tagline">Gathering<br>Gentle Meadow Corners</div>
    </div>
    <div class="contact-block">
      <div class="person-name">Marguerite Holloway</div>
      <div class="contact-line">0419 862 503</div>
      <div class="contact-line">marguerite@amberburrows.com.au</div>
      <div class="contact-line">www.amberburrows.com.au</div>
    </div>
  </section>
</main>
</body>
</html>
```